Website home page re-design

I have a brochure website www.baylorwick-suites.com that allows customers to buy my product (rent meeting room or work space by the hour/day, etc or sign up for virtual office services). The mechanical aspects of the site are done and working... I just want a different, more market "correct" image on the site built around my logo, tag line and them colors (royal blue and kelly green).

Industry/Entity Type

Product

```html
<!DOCTYPE html>
<html lang="en">
<head>
<meta charset="utf-8">
<title>Baylorwick Suites</title>
<link href="https://fonts.googleapis.com/css2?family=Open+Sans:ital,wght@0,400;0,600;0,700;1,700&display=swap" rel="stylesheet">
<style>
:root{
  --blue:#1f4fbf;
  --blue-dark:#173d96;
  --green:#1db24b;
  --green-dark:#14963c;
  --ink:#333;
  --muted:#666;
  --rule:#e3e3e3;
  --footer:#3d3d3d;
  --footer-deep:#2c2c2c;
}
*{box-sizing:border-box;margin:0;padding:0}
html,body{width:719px;height:1200px;overflow:hidden;background:#fff}
body{font-family:"Open Sans",Arial,sans-serif;color:var(--ink);font-size:8px;line-height:1.45}
.page{width:719px;height:1200px;position:relative;overflow:hidden}
.topbar{height:14px;background:var(--green);display:flex;justify-content:space-between;align-items:center;padding:0 22px;color:#fff;font-size:6.5px}
.topbar .links span{margin-left:10px;font-weight:600}
.topbar .links span.active{background:var(--green-dark);padding:1px 5px}
.nav{height:36px;display:flex;justify-content:space-between;align-items:center;padding:0 22px;border-bottom:1px solid var(--rule)}
.brand{display:flex;align-items:center;gap:5px;font-weight:700;font-size:17px;color:var(--blue)}
.brand .dot{width:14px;height:14px;border-radius:50%;background:var(--green)}
.menu{display:flex;gap:3px}
.menu a{font-size:7px;color:var(--ink);text-decoration:none;padding:5px 7px;font-weight:600}
.menu a.current{background:var(--blue);color:#fff}
.hero{height:250px;position:relative;background:linear-gradient(180deg,#c7ccd2 0%,#7b838e 45%,#3b3f47 100%)}
.hero p{position:absolute;left:34px;bottom:22px;color:#fff;font-style:italic;font-weight:700;font-size:12.5px;line-height:1.35;width:470px;text-shadow:0 1px 2px rgba(0,0,0,.5)}
.about{display:flex;gap:26px;padding:22px 34px 18px}
.about h2,.tour h2,.services h2,.video h2{font-size:15px;color:var(--ink);font-weight:600;margin-bottom:6px;display:flex;align-items:center;gap:5px}
.about h2 .mini{color:var(--blue);font-weight:700}
.about h2 .mini::before{content:"";display:inline-block;width:10px;height:10px;border-radius:50%;background:var(--green);margin-right:3px;vertical-align:-1px}
.about .copy{width:320px;color:var(--muted);font-size:7px}
.tour{width:300px}
.player{height:118px;background:linear-gradient(160deg,#8d96a3,#3f4650);position:relative}
.player .bar{position:absolute;left:0;right:0;bottom:0;height:12px;background:rgba(0,0,0,.6);display:flex;align-items:center;padding:0 5px;gap:5px}
.player .bar i{display:block;width:0;height:0;border-left:5px solid #fff;border-top:3px solid transparent;border-bottom:3px solid transparent}
.player .bar b{flex:1;height:2px;background:#999}
.services{padding:6px 34px 0;border-top:1px solid var(--rule);margin:0 0}
.services h2{margin-top:10px}
.grid{display:grid;grid-template-columns:repeat(3,1fr);row-gap:22px;padding:10px 30px 0}
.svc{display:flex;align-items:center;gap:9px}
.svc .ring{width:44px;height:44px;border-radius:50%;border:2px solid var(--green);display:flex;align-items:center;justify-content:center;flex:none}
.svc span{color:var(--green);font-weight:700;font-size:8px}
.more{display:block;width:46px;margin:22px auto 0;background:var(--blue);color:#fff;font-size:7px;text-align:center;padding:4px 0;font-weight:600}
.band{margin-top:20px;height:96px;background:var(--green);display:flex;align-items:center;justify-content:space-between;padding:0 34px}
.band p{color:#fff;font-style:italic;font-weight:700;font-size:12px;line-height:1.4;width:440px}
.band .cta{border:2px solid #fff;color:#fff;font-size:11px;font-weight:600;padding:8px 18px}
.video{padding:18px 34px 0}
.video .row{display:flex;gap:16px;margin-top:6px}
.video .shot{width:170px;height:110px;background:linear-gradient(160deg,#c9ced6,#6b7480);flex:none}
.video .copy{color:var(--muted);font-size:7px}
.video .copy p+p{margin-top:6px}
.video .read{display:block;width:44px;margin:8px 0 0 auto;background:var(--blue);color:#fff;text-align:center;font-size:7px;padding:3px 0;font-weight:600}
.footer{position:absolute;left:0;right:0;top:998px;height:178px;background:var(--footer);color:#ddd;display:flex;padding:18px 34px;gap:40px}
.footer h3{font-size:8px;color:#fff;font-weight:700;margin-bottom:8px}
.footer ul{list-style:none;font-size:6.5px;line-height:1.9}
.footer li::before{content:"› ";color:var(--green)}
.contact div{display:flex;align-items:center;gap:5px;font-size:6.5px;margin-bottom:7px}
.contact svg{flex:none}
.hours table{font-size:6.5px;border-collapse:collapse}
.hours td{padding:1px 12px 1px 0}
.badge{position:absolute;right:40px;top:28px;width:86px;height:86px;border-radius:50%;background:#555}
.legal{position:absolute;left:0;right:0;bottom:0;height:24px;background:var(--footer-deep);color:#aaa;font-size:6px;display:flex;align-items:center;padding:0 34px}
</style>
</head>
<body>
<div class="page">
  <div class="topbar">
    <span>www.baylorwick-suites.com</span>
    <div class="links"><span>Digital Reception Center</span><span>Business &amp; Professional Center</span><span class="active">My Account</span></div>
  </div>
  <header class="nav">
    <div class="brand"><span class="dot"></span>Baylorwick</div>
    <nav class="menu">
      <a class="current">Home</a><a>Video Conference Service</a><a>Our iServices</a><a>Book An Event</a><a>Contact Us</a>
    </nav>
  </header>

  <section class="hero" role="img" aria-label="Photo of a business team meeting around a conference table">
    <p>Lorem ipsum dolor sit amet, consectetuer adipiscing elit, sed diam nonummy nibh euismod tincidunt ut laoreet</p>
  </section>

  <section class="about">
    <div class="copy">
      <h2>About <span class="mini">Baylorwick</span></h2>
      <p>Baylorwick is a full service virtual workspace built to meet the needs of attorneys, mediators, paralegals, court reporters and business professionals of all kinds. Realtors, small business owners, trainers, insurance agents and home-based sales reps rent our rooms by the hour or day. We host meetings, depositions, arbitration, interviews and video conference sessions in a calm, private setting with a friendly staff ready to help you every step of the way, guaranteed.</p>
    </div>
    <div class="tour">
      <h2>Virtual Tour Vedio</h2>
      <div class="player" role="img" aria-label="Video still of a meeting room tour">
        <div class="bar"><i></i><b></b></div>
      </div>
    </div>
  </section>

  <section class="services">
    <h2>Our iServices</h2>
    <div class="grid">
      <div class="svc"><div class="ring"><svg width="22" height="22" viewBox="0 0 24 24" fill="none" stroke="#1f4fbf" stroke-width="2"><path d="M3 11l9-7 9 7"/><path d="M6 10v10h12V10"/><rect x="10" y="14" width="4" height="6"/></svg></div><span>Work-From-Home<br>Professionals</span></div>
      <div class="svc"><div class="ring"><svg width="22" height="22" viewBox="0 0 24 24" fill="none" stroke="#1f4fbf" stroke-width="2"><path d="M4 12l8-7 8 7"/><path d="M6 11v9h12v-9"/><circle cx="12" cy="14" r="2"/></svg></div><span>Real Estate Agents</span></div>
      <div class="svc"><div class="ring"><svg width="22" height="22" viewBox="0 0 24 24" fill="none" stroke="#1f4fbf" stroke-width="2"><path d="M3 12a9 8 0 0 1 18 0z"/><path d="M12 12v7a2 2 0 0 1-4 0"/></svg></div><span>Insurance Agents</span></div>
      <div class="svc"><div class="ring"><svg width="22" height="22" viewBox="0 0 24 24" fill="none" stroke="#1f4fbf" stroke-width="2"><rect x="4" y="5" width="16" height="11" rx="1"/><path d="M8 20h8M12 16v4M7 9h10M7 12h6"/></svg></div><span>Court Reporters</span></div>
      <div class="svc"><div class="ring"><svg width="22" height="22" viewBox="0 0 24 24" fill="none" stroke="#1f4fbf" stroke-width="2"><path d="M6 3h9l4 4v14H6z"/><path d="M9 10h7M9 14h7M9 18h4"/></svg></div><span>Claims Adjusters</span></div>
      <div class="svc"><div class="ring"><svg width="22" height="22" viewBox="0 0 24 24" fill="none" stroke="#1f4fbf" stroke-width="2"><path d="M12 3v18M7 21h10M4 7h16"/><path d="M4 7l-3 7h6zM20 7l-3 7h6z"/></svg></div><span>Attorneys</span></div>
    </div>
    <a class="more">View All</a>
  </section>

  <section class="band">
    <p>Lorem ipsum dolor sit amet, consectetuer adipiscing elit, sed diam nonummy nibh euismod tincidunt ut laoreet</p>
    <span class="cta">Book An Event</span>
  </section>

  <section class="video">
    <h2>Video Conference Service</h2>
    <div class="row">
      <div class="shot" role="img" aria-label="Photo of a group joining a video conference call"></div>
      <div class="copy">
        <p>Video conferencing is available in and hosted virtually by Baylorwick. Aligning several busy schedules is never an easy task, whether or not the participants are located in the same area. With our video conferencing you can more easily schedule conferences, interviews, depositions, arbitration, mediation and other meetings. Why not let us take the stress out of your next gathering?</p>
        <p>Save time, money, travel and frustration. Our video conferencing lets you avoid the cost and inconvenience of business travel.</p>
        <a class="read">Read More</a>
      </div>
    </div>
  </section>

  <footer class="footer">
    <div>
      <h3>Quick Links</h3>
      <ul><li>Home</li><li>Video Conference Service</li><li>Our iServices</li><li>Book An Event</li><li>Contact Us</li></ul>
    </div>
    <div class="contact">
      <h3>Contact Details</h3>
      <div><svg width="8" height="8" viewBox="0 0 24 24" fill="#1db24b"><path d="M12 2a7 7 0 0 0-7 7c0 5 7 13 7 13s7-8 7-13a7 7 0 0 0-7-7zm0 9.5A2.5 2.5 0 1 1 12 6.5a2.5 2.5 0 0 1 0 5z"/></svg><span>418 Alder Row<br>Brookfield, TN 37000</span></div>
      <div><svg width="8" height="8" viewBox="0 0 24 24" fill="#1db24b"><path d="M6.6 10.8a15 15 0 0 0 6.6 6.6l2.2-2.2a1 1 0 0 1 1-.25 11.4 11.4 0 0 0 3.6.6 1 1 0 0 1 1 1V20a1 1 0 0 1-1 1A17 17 0 0 1 3 4a1 1 0 0 1 1-1h3.5a1 1 0 0 1 1 1 11.4 11.4 0 0 0 .6 3.6 1 1 0 0 1-.25 1z"/></svg><span>800-555-0142</span></div>
      <div><svg width="8" height="8" viewBox="0 0 24 24" fill="#1db24b"><path d="M2 5h20v14H2z"/><path d="M2 5l10 8 10-8" stroke="#3d3d3d" stroke-width="2" fill="none"/></svg><span>info@baylorwick-suites.com</span></div>
    </div>
    <div class="hours">
      <h3>Business Hours</h3>
      <table>
        <tr><td>Mon</td><td>8 am to 6 pm</td></tr>
        <tr><td>Tue</td><td>8 am to 6 pm</td></tr>
        <tr><td>Wed</td><td>8 am to 6 pm</td></tr>
        <tr><td>Thu</td><td>8 am to 6 pm</td></tr>
        <tr><td>Fri</td><td>8 am to 6 pm</td></tr>
        <tr><td>Sat</td><td>Closed</td></tr>
        <tr><td>Sun</td><td>Closed</td></tr>
      </table>
    </div>
    <div class="badge"></div>
  </footer>
  <div class="legal">© Baylorwick 2015 | All Rights Reserved</div>
</div>
</body>
</html>
```